Meridale Legal Letterhead for Law firm must be modern and use the logo I uploaded.

Hello I want a clean modern professional letterhead for my law firm Meridale Legal. A logo has already been created and all files have been uploaded. The information for the firm can be given through message. Please use the logo that has already been created. Please also use the color scheme of that logo. (blue and white).

Target Market(s)

General Public

Industry/Entity Type

Law Firm

Colors

Designer to choose colors to be used in the design.

Requirements
Must have
• This must be a modern professional letterhead
Nice to have
• My logo that is included in file form
Should not have
• Should not have logo that is not the one I uploaded.

```html
<!DOCTYPE html>
<html lang="en">
<head>
<meta charset="utf-8">
<title>Meridale Legal Letterhead</title>
<link href="https://fonts.googleapis.com/css2?family=Roboto:wght@300;500&family=Tinos:wght@400;700&display=swap" rel="stylesheet">
<style>
  :root {
    --backdrop: #cccccc;
    --paper: #ffffff;
    --navy: #2d3262;
    --ink: #333333;
    --muted: #5f5f5f;
    --footer-text: #ffffff;
  }
  * { margin: 0; padding: 0; box-sizing: border-box; }
  html, body {
    width: 1150px;
    height: 1200px;
    overflow: hidden;
    background: var(--backdrop);
  }
  .letterhead {
    position: absolute;
    left: 190px;
    top: 102px;
    width: 769px;
    height: 996px;
    background: var(--paper);
    font-family: "Tinos", "Times New Roman", serif;
  }
  .brand-name {
    position: absolute;
    top: 138px;
    left: 0;
    width: 100%;
    text-align: center;
    font-family: "Roboto", Arial, sans-serif;
    font-weight: 500;
    font-size: 20px;
    letter-spacing: 0.62em;
    text-indent: 0.62em;
    color: var(--navy);
    text-transform: uppercase;
  }
  .letter-meta {
    position: absolute;
    top: 222px;
    right: 99px;
    text-align: right;
    color: var(--muted);
    font-size: 15px;
  }
  .letter-date { margin-bottom: 10px; }
  .recipient { line-height: 20px; }
  .recipient-name { font-weight: 700; }
  .letter-body {
    position: absolute;
    top: 370px;
    left: 118px;
    width: 552px;
    color: var(--ink);
    font-size: 14.6px;
    line-height: 25px;
    text-align: justify;
  }
  .letter-body p + p { margin-top: 25px; }
  .contact-band {
    position: absolute;
    left: 0;
    bottom: 0;
    width: 100%;
    height: 71px;
    background: var(--navy);
    font-family: "Roboto", Arial, sans-serif;
    font-weight: 300;
    font-size: 12.4px;
    color: var(--footer-text);
  }
  .contact-item {
    position: absolute;
    top: 0;
    height: 71px;
    display: flex;
    align-items: center;
    gap: 12px;
  }
  .contact-item svg { width: 14px; height: 14px; flex: none; }
  .contact-address { left: 118px; }
  .contact-phone { left: 381px; }
  .contact-web { left: 543px; }
</style>
</head>
<body>
  <main class="letterhead">
    <header>
      <div class="brand-name">Meridale Legal</div>
    </header>

    <section class="letter-meta">
      <p class="letter-date">November 16, 2023</p>
      <address class="recipient" style="font-style:normal">
        <div class="recipient-name">Recippient Name</div>
        <div>Vice President</div>
        <div>Example Incooration</div>
        <div>State</div>
      </address>
    </section>

    <article class="letter-body">
      <p>Lorem ipsum dolor sit amet, consectetur adipiscing elit. Phasellus nec velit sed ligula facilisis malesuada interdum non urna. Aliquam auctor eros sed gravida viverra. Mauris fringilla ac elit vitae laoreet. Integer condimentum vel lectus non eleifend. Quisque facilisis faucibus blandit. Proin vestibulum dapibus ipsum eu commodo. Nullam hendrerit lectus nec lectus venenatis mattis.</p>
      <p>Vestibulum ornare lorem sed feugiat faucibus. Morbi efficitur sapien ut tellus pellentesque, a lacinia nisi fermentum. Sed viverra mi lacus, ac scelerisque nisl fringilla at. Nullam lectus ipsum, laoreet ac libero eget, dapibus faucibus magna. Orci varius natoque penatibus et magnis dis parturient montes, nascetur ridiculus mus. Integer in posuere orci. Pellentesque euismod ut ante eu elementum. Ut consectetur ac urna sed varius.Aliquam consectetur tortor erat, non aliquet libero accumsan id.</p>
      <p>Nunc magna purus, fermentum ut nulla vitae, aliquet placerat urna. Donec leo justo, ornare quis lectus sit amet, aliquam venenatis diam. Vivamus pharetra dui ut quam sagittis dignissim. Aliquam eget turpis purus. Aliquam erat volutpat. Etiam sed ultricies purus, bibendum porttitor neque.</p>
    </article>

    <footer class="contact-band">
      <div class="contact-item contact-address">
        <svg viewBox="0 0 14 14" aria-hidden="true">
          <circle cx="7" cy="7" r="7" fill="#fff"/>
          <path d="M7 3.2a2.6 2.6 0 0 0-2.6 2.6C4.4 7.8 7 10.8 7 10.8s2.6-3 2.6-5A2.6 2.6 0 0 0 7 3.2z" fill="var(--navy)"/>
          <circle cx="7" cy="5.8" r="1" fill="#fff"/>
        </svg>
        <span>Name of Street, City, Province, Country</span>
      </div>
      <div class="contact-item contact-phone">
        <svg viewBox="0 0 14 14" aria-hidden="true">
          <circle cx="7" cy="7" r="7" fill="#fff"/>
          <path d="M4.6 3.6l1.2-.2.8 1.8-.8.7c.4.9 1.2 1.7 2.1 2.1l.7-.8 1.8.8-.2 1.2c-.1.4-.5.6-.9.6C6.4 9.6 4.4 7.6 4 4.5c0-.4.2-.8.6-.9z" fill="var(--navy)"/>
        </svg>
        <span>00 123 456 789</span>
      </div>
      <div class="contact-item contact-web">
        <svg viewBox="0 0 14 14" aria-hidden="true" fill="none" stroke="#fff" stroke-width="1">
          <circle cx="7" cy="7" r="6.2"/>
          <ellipse cx="7" cy="7" rx="2.8" ry="6.2"/>
          <line x1="0.8" y1="7" x2="13.2" y2="7"/>
          <line x1="1.8" y1="4" x2="12.2" y2="4"/>
          <line x1="1.8" y1="10" x2="12.2" y2="10"/>
        </svg>
        <span>www.meridalelegal.com</span>
      </div>
    </footer>
  </main>
</body>
</html>
```